New Business Card

Would like a shiny card with Metallic logo raised on th front. Address 518 Whitlock Avenue, Toronto Ontario M4K2J8, phone 416 555 0182, email kvbe@lindenmail.ca and web www.kvbe.ca on the back in right and left lower corners balanced. Top of back should say Personalized Care for Pet's and their People centered. Leaving space on the back to write. Horizontal placement

Industry/Entity Type

Business

```html
<!DOCTYPE html>
<html lang="en">
<head>
<meta charset="utf-8">
<title>Whitlock Avenue Animal Hospital – Business Card</title>
<link href="https://fonts.googleapis.com/css2?family=Montserrat:wght@400;600&family=Work+Sans:wght@400;500&display=swap" rel="stylesheet">
<style>
  :root {
    --backdrop: #141414;
    --card: #1f1f1f;
    --card-edge: #2a2a2a;
    --ink: #f4f4f4;
    --ink-soft: #d9d9d9;
  }
  * { box-sizing: border-box; margin: 0; padding: 0; }
  html, body {
    width: 1200px; height: 900px; overflow: hidden;
    background: var(--backdrop);
  }
  .sheet {
    width: 1200px; height: 900px;
    display: flex; flex-direction: column; align-items: center; justify-content: center;
    gap: 40px;
  }
  .card {
    width: 740px; height: 390px;
    background: linear-gradient(135deg, #262626 0%, var(--card) 55%, #1a1a1a 100%);
    border: 1px solid var(--card-edge);
    color: var(--ink);
    position: relative;
  }
  /* Front */
  .card--front {
    display: flex; flex-direction: column; align-items: center; justify-content: center;
  }
  .brand { display: flex; flex-direction: column; align-items: center; }
  .brand__dot {
    width: 78px; height: 78px; border-radius: 50%;
    background: var(--ink); margin-bottom: 18px;
  }
  .brand__name {
    font-family: "Montserrat", sans-serif; font-weight: 600;
    font-size: 26px; letter-spacing: 1px; text-transform: uppercase;
    text-align: center; line-height: 1.2;
  }
  .tagline {
    margin-top: 30px;
    font-family: "Montserrat", sans-serif; font-weight: 600;
    font-size: 16px; letter-spacing: 2px; text-transform: uppercase;
    text-align: center; line-height: 1.35; color: var(--ink-soft);
  }
  /* Back */
  .card--back {
    display: flex; align-items: center; padding: 0 48px 0 40px;
  }
  .card--back .brand { width: 330px; }
  .card--back .brand__name { font-size: 22px; }
  .divider {
    width: 2px; height: 200px; background: var(--ink);
    margin: 0 36px 0 30px;
  }
  .contact { font-family: "Work Sans", sans-serif; color: var(--ink); }
  .contact__name {
    font-family: "Montserrat", sans-serif; font-weight: 600;
    font-size: 22px; letter-spacing: 1.5px; text-transform: uppercase;
  }
  .contact__role { font-size: 17px; color: var(--ink-soft); margin-top: 2px; }
  .contact__address { font-size: 16px; line-height: 1.35; margin-top: 18px; }
  .contact__list { list-style: none; margin-top: 14px; }
  .contact__list li {
    display: flex; align-items: center; gap: 12px;
    font-size: 16px; line-height: 1.6;
  }
  .contact__list svg { width: 15px; height: 15px; flex: none; }
</style>
</head>
<body>
  <main class="sheet">
    <section class="card card--front">
      <div class="brand">
        <span class="brand__dot"></span>
        <p class="brand__name">Whitlock Avenue<br>Animal Hospital</p>
      </div>
      <p class="tagline">Personalized care for pet's<br>and their people centered</p>
    </section>

    <section class="card card--back">
      <div class="brand">
        <span class="brand__dot"></span>
        <p class="brand__name">Whitlock Avenue<br>Animal Hospital</p>
      </div>
      <span class="divider"></span>
      <div class="contact">
        <p class="contact__name">Darren Okafor</p>
        <p class="contact__role">Founder</p>
        <p class="contact__address">518 Whitlock Avenue,<br>Toronto Ontario M4K2J8</p>
        <ul class="contact__list">
          <li>
            <svg viewBox="0 0 24 24" aria-hidden="true"><path fill="#f4f4f4" d="M6.6 10.8a15.1 15.1 0 0 0 6.6 6.6l2.2-2.2a1 1 0 0 1 1-.25 11.4 11.4 0 0 0 3.6.57 1 1 0 0 1 1 1V20a1 1 0 0 1-1 1A17 17 0 0 1 3 4a1 1 0 0 1 1-1h3.5a1 1 0 0 1 1 1c0 1.25.2 2.45.57 3.57a1 1 0 0 1-.25 1z"/></svg>
            416 555 0182
          </li>
          <li>
            <svg viewBox="0 0 24 24" aria-hidden="true"><rect x="2" y="5" width="20" height="14" fill="#f4f4f4"/><path d="M2 5l10 8 10-8" fill="none" stroke="#1f1f1f" stroke-width="2"/></svg>
            kvbe@lindenmail.ca
          </li>
          <li>
            <svg viewBox="0 0 24 24" aria-hidden="true" fill="none" stroke="#f4f4f4" stroke-width="2"><circle cx="12" cy="12" r="9.5"/><ellipse cx="12" cy="12" rx="4.5" ry="9.5"/><path d="M2.5 12h19"/></svg>
            www.kvbe.ca
          </li>
        </ul>
      </div>
    </section>
  </main>
</body>
</html>
```